Plumvale CEO needs a Crowdsourced Graphic for a Wirelark Article

I need a simple graphic / banner for a blog post that's going to be posted on Wirelark (www.wirelark.com) - the biggest tech blog in the world.

The article will be written by Tobin Marsh (Plumvale's CEO) and the title will be "Asia's Secret Crowdsourcing Boom". The article is about the tens of thousands of people using crowdsourcing websites (like Plumvale.com, Qorvel.com and Vantrio.com) in China, India, the Philippines, Australia and other countries in the Asia Pacific region.

We'd really like to get this ASAP - so early submissions encouraged. We will try and get the winning designer linked to from the article.

Thanks to everyone that submitted!  Some great designs and hard to choose! :)

Target Market(s)

Tech saavy readers, English speakers

Industry/Entity Type

Tech

Requirements
Must have
• The graphic SHOULD:
1) Have the text "Asia's secret crowdsourcing boom" with some nice design and fonts (consider grey subtle pattern background and white drop shadow on fonts) - see attached examples
2) Have an Asian theme
3) Have the dimensions 640px wide by 240px wide
Nice to have
• The graphic COULD:
1) Have references to some or all of the countries mentioned above or use Asian characters as part of the background / motif (maybe the word "crowd" or "crowd sourcing" in different languages). In Chinese, the word for crowdsourcing is "witkey" (and there are corresponding Chinese characters: ??)
2) Emphasize the word "Asia" (using color and larger/different font)
3) Use a chart showing exponential (i.e. fast) growth - like the attached
4) Have a second line of text "5 Things You Didn't Know About Crowdsourcing in Asia"

```html
<!DOCTYPE html>
<html lang="en">
<head>
<meta charset="utf-8">
<title>Asia's Secret Crowdsourcing Boom</title>
<link rel="stylesheet" href="https://fonts.googleapis.com/css2?family=Source+Sans+3:wght@300;400;700&display=swap">
<style>
  :root {
    --page-bg: #ffffff;
    --banner-dark: #1c2121;
    --banner-mid: #5f6464;
    --banner-light: #a89c9c;
    --banner-rose: #b9a9a8;
    --motif-dark: rgba(120, 135, 135, 0.22);
    --motif-light: rgba(110, 90, 92, 0.28);
    --grid-line: rgba(170, 185, 185, 0.28);
    --accent-yellow: #f7e000;
    --title-white: #ffffff;
    --shadow-dark: rgba(0, 0, 0, 0.6);
  }
  * { margin: 0; padding: 0; box-sizing: border-box; }
  html, body {
    width: 1200px;
    height: 900px;
    overflow: hidden;
    background: var(--page-bg);
  }
  .canvas {
    position: relative;
    width: 1200px;
    height: 900px;
  }
  .banner {
    position: absolute;
    left: 225px;
    top: 320px;
    width: 768px;
    height: 288px;
    overflow: hidden;
    font-family: "Source Sans 3", "Myriad Pro", sans-serif;
  }
  .banner-backdrop {
    position: absolute;
    inset: 0;
    background: linear-gradient(90deg,
      var(--banner-dark) 0%,
      #2f3535 22%,
      var(--banner-mid) 42%,
      var(--banner-light) 66%,
      var(--banner-rose) 100%);
  }
  .banner-motif {
    position: absolute;
    inset: 0;
    background:
      radial-gradient(ellipse 140px 170px at 110px 150px, var(--motif-dark), transparent 70%),
      radial-gradient(ellipse 130px 160px at 300px 230px, var(--motif-dark), transparent 70%),
      radial-gradient(ellipse 170px 190px at 520px 120px, var(--motif-light), transparent 70%),
      radial-gradient(ellipse 160px 180px at 700px 200px, var(--motif-light), transparent 70%);
  }
  .banner-grid {
    position: absolute;
    inset: 0;
    width: 768px;
    height: 288px;
  }
  .emblem {
    position: absolute;
    left: 511px;
    top: 62px;
    width: 66px;
    height: 66px;
  }
  .headline {
    position: absolute;
    left: 37px;
    top: 82px;
    white-space: nowrap;
    line-height: 1;
  }
  .headline-accent {
    font-weight: 700;
    font-size: 84px;
    color: var(--accent-yellow);
    text-shadow: 1px 2px 3px var(--shadow-dark);
  }
  .headline-rest {
    font-weight: 300;
    font-size: 39px;
    color: var(--title-white);
    margin-left: 10px;
    text-shadow: 1px 1px 2px var(--shadow-dark);
  }
  .subtitle {
    position: absolute;
    left: 278px;
    top: 160px;
    font-weight: 700;
    font-size: 19px;
    letter-spacing: -0.2px;
    color: var(--accent-yellow);
    white-space: nowrap;
    text-shadow: 1px 1px 2px var(--shadow-dark);
  }
</style>
</head>
<body>
  <main class="canvas">
    <section class="banner">
      <div class="banner-backdrop"></div>
      <div class="banner-motif" role="img" aria-label="Faint ornamental Asian scrollwork pattern over a textured grey-to-rose background"></div>
      <svg class="banner-grid" viewBox="0 0 768 288" aria-hidden="true">
        <g stroke="var(--grid-line)" stroke-width="2" fill="none">
          <line x1="75" y1="0" x2="75" y2="288"/>
          <line x1="268" y1="0" x2="268" y2="288"/>
          <line x1="0" y1="30" x2="420" y2="30"/>
          <line x1="0" y1="174" x2="420" y2="174"/>
        </g>
      </svg>
      <svg class="emblem" viewBox="0 0 66 66" role="img" aria-label="Yin and yang symbol">
        <circle cx="33" cy="33" r="30" fill="none" stroke="var(--accent-yellow)" stroke-width="2.5"/>
        <path d="M33 3 A30 30 0 0 1 33 63 A15 15 0 0 1 33 33 A15 15 0 0 0 33 3 Z" fill="var(--accent-yellow)"/>
        <circle cx="33" cy="18" r="4" fill="var(--accent-yellow)"/>
        <circle cx="33" cy="48" r="4" fill="var(--banner-light)"/>
      </svg>
      <h1 class="headline">
        <span class="headline-accent">Asia's</span><span class="headline-rest">Secret Crowdsourcing Boom</span>
      </h1>
      <p class="subtitle">5 Things You Didn't Know About Crowdsourcing in Asia</p>
    </section>
  </main>
</body>
</html>
```